Business Card Design

We would like to re-design our business cards. Our Company - Quarvel Turbochargers, rebuilds turbochargers and sells replacement parts. Our website is: http://www.quarvelturbochargers.example
We just had our logo changed. I will attach the file. Looking for fresh new/modern business card. We like the colors red, black, white and silver. Black background looks attractive, but not a requirement. The final design should communicate reasonable/competitive prices, top quality and reliability of our products.
Updates
Project Deadline Extended
Reason: Need to finalize the info on the card. Currently working on changing address and email info. Want to make sure it is the correct one before accepting the final design. Unless, this is something that can be changed at a later time..??
Industry/Entity Type
Business
Contact Information for Business Card
QUARVEL TURBOCHARGERS, LLC
20473 Harrow Bend SE
Massillon, OH 44902
Tel: +1-330-555-0142
Fax: +1-330-555-0187
info@QuarvelTurbochargers.example
Our current business card had the following highlights:
*We rebuild all Turbocharges for Automotive, Diesel and Industrial
*Precision Balancing and in-house turbocharger needs
*All Turbocharger replacement parts are made in USA / U.K.
Look and feel
Each slider illustrates characteristics of the customer's brand and the style your logo design should communicate.

```html
<!DOCTYPE html>
<html lang="en">
<head>
<meta charset="utf-8">
<title>Quarvel Turbochargers – Business Card</title>
<link rel="stylesheet" href="https://fonts.googleapis.com/css2?family=Montserrat:wght@400;500;600;700&display=swap">
<style>
  :root {
    --backdrop: #c9c9c9;
    --card-black: #0d0d0d;
    --card-black-soft: #1a1a1a;
    --brand-red: #e0232a;
    --text-white: #f4f4f4;
    --divider: #2e2e2e;
  }
  * { box-sizing: border-box; margin: 0; padding: 0; }
  html, body {
    width: 1200px;
    height: 900px;
    overflow: hidden;
    background: var(--backdrop);
    font-family: "Montserrat", Arial, sans-serif;
  }
  .sheet {
    width: 1200px;
    height: 900px;
    display: flex;
    flex-direction: column;
    align-items: center;
    justify-content: center;
    gap: 44px;
  }
  .card {
    position: relative;
    width: 560px;
    height: 320px;
    background: radial-gradient(ellipse at 55% 35%, var(--card-black-soft), var(--card-black) 70%);
    box-shadow: 0 6px 18px rgba(0,0,0,0.25);
    overflow: hidden;
  }
  .brand {
    position: absolute;
    display: flex;
    align-items: center;
    gap: 10px;
    color: var(--text-white);
    font-weight: 700;
    letter-spacing: 0.5px;
    white-space: nowrap;
  }
  .brand-mark {
    width: 18px;
    height: 18px;
    background: var(--brand-red);
    flex: none;
  }
  .card-front .brand {
    left: 50%;
    top: 50%;
    transform: translate(-50%, -50%);
    font-size: 24px;
  }
  .card-back .brand {
    right: 44px;
    top: 58px;
    font-size: 18px;
  }
  .card-back .brand-mark { width: 14px; height: 14px; }
  .holder {
    position: absolute;
    left: 40px;
    top: 104px;
  }
  .holder-name {
    color: var(--text-white);
    font-size: 23px;
    font-weight: 500;
    letter-spacing: 0.3px;
  }
  .holder-title {
    color: var(--brand-red);
    font-size: 13px;
    font-weight: 500;
    margin-top: 2px;
  }
  .divider {
    position: absolute;
    left: 40px;
    right: 40px;
    top: 178px;
    height: 1px;
    background: linear-gradient(90deg, transparent, var(--divider) 30%, var(--divider) 70%, transparent);
  }
  .contacts {
    position: absolute;
    right: 40px;
    bottom: 28px;
    list-style: none;
    text-align: right;
  }
  .contact {
    display: flex;
    align-items: center;
    justify-content: flex-end;
    gap: 10px;
    color: var(--text-white);
    font-size: 14px;
    line-height: 22px;
    letter-spacing: 0.3px;
  }
  .contact-icon {
    width: 11px;
    height: 11px;
    flex: none;
    fill: var(--brand-red);
    stroke: var(--brand-red);
  }
</style>
</head>
<body>
<main class="sheet">
  <section class="card card-front" aria-label="Business card front">
    <div class="brand"><span class="brand-mark"></span>Quarvel Turbochargers</div>
  </section>

  <section class="card card-back" aria-label="Business card back">
    <div class="brand"><span class="brand-mark"></span>Quarvel Turbochargers</div>
    <div class="holder">
      <p class="holder-name">Daniel Pierce</p>
      <p class="holder-title">Managing Director</p>
    </div>
    <div class="divider"></div>
    <ul class="contacts">
      <li class="contact">123.456.7890
        <svg class="contact-icon" viewBox="0 0 12 12" aria-hidden="true"><rect x="3" y="0.5" width="6" height="11" rx="1" fill="none" stroke-width="1.2"/><circle cx="6" cy="9.5" r="0.7" stroke="none"/></svg>
      </li>
      <li class="contact">123.456.7890
        <svg class="contact-icon" viewBox="0 0 12 12" aria-hidden="true"><path d="M1 4 C1 2 3 1.5 6 1.5 S11 2 11 4 L8.5 4.5 L8 3.5 H4 L3.5 4.5 Z" stroke="none"/><rect x="2.5" y="6" width="7" height="5" rx="1" stroke="none"/></svg>
      </li>
      <li class="contact">info@youremail.com
        <svg class="contact-icon" viewBox="0 0 12 12" aria-hidden="true"><rect x="0.5" y="2" width="11" height="8" rx="1" stroke="none"/><path d="M1 2.5 L6 6.5 L11 2.5" fill="none" stroke="#0d0d0d" stroke-width="1"/></svg>
      </li>
      <li class="contact">www.website.com
        <svg class="contact-icon" viewBox="0 0 12 12" aria-hidden="true"><rect x="0.8" y="4.5" width="6" height="3.5" rx="1.75" fill="none" stroke-width="1.2" transform="rotate(-45 3.8 6.25)"/><rect x="5.2" y="4" width="6" height="3.5" rx="1.75" fill="none" stroke-width="1.2" transform="rotate(-45 8.2 5.75)"/></svg>
      </li>
    </ul>
  </section>
</main>
</body>
</html>
```